New customer flyer

Looking for a flyer that can be written on as a field estimate for door to door sales
Ideally have some nice on the front with the back as a estimate form
Doorknob hanger size

Target Market(s)

Home owners buying core aeration service

Industry/Entity Type

Lawn Care

Requirements
Must have
• Logo
• First name
• Last name
• Cell
• Email
• Address
• Sq ft
Nice to have
• Benefits of core aeration

```html
<!DOCTYPE html>
<html lang="en">
<head>
<meta charset="utf-8">
<title>TurfVent – Doorknob Flyer</title>
<link href="https://fonts.googleapis.com/css2?family=Montserrat:wght@500;600;700&display=swap" rel="stylesheet">
<style>
  :root{
    --brand-blue:#3567b1;
    --brand-green:#4a8c3a;
    --grass-dark:#3c8527;
    --grass-light:#7dc445;
    --paper:#ffffff;
    --backdrop:#f3f5f1;
    --edge:#b9c9e3;
    --tagline:#444444;
  }
  html,body{margin:0;padding:0;}
  body{
    width:927px;height:1200px;overflow:hidden;
    background:var(--backdrop);
    font-family:"Montserrat",sans-serif;
    position:relative;
  }
  .flyer-page{
    position:absolute;top:325px;width:425px;height:549px;
    background:var(--paper);
    outline:1px solid var(--edge);
  }
  .flyer-front{left:26px;}
  .flyer-back{left:476px;}
  .flyer-page svg{display:block;width:100%;height:100%;}
  .fill-blue{fill:var(--brand-blue);}
  .fill-green{fill:var(--brand-green);}
  .fill-paper{fill:var(--paper);}
  .brand-name{font-family:"Montserrat",sans-serif;font-weight:600;fill:var(--brand-blue);}
  .brand-tagline{font-family:"Montserrat",sans-serif;font-weight:500;fill:var(--tagline);}
  .contact-line{font-family:"Montserrat",sans-serif;font-weight:700;font-size:13px;fill:#fff;}
  .field-box{fill:#fff;stroke:var(--brand-blue);stroke-width:2;}
  .field-label{font-family:"Montserrat",sans-serif;font-weight:700;font-size:9.5px;fill:#fff;}
</style>
</head>
<body>

<!-- Front of the doorknob flyer -->
<section class="flyer-page flyer-front">
  <svg viewBox="0 0 584 755" xmlns="http://www.w3.org/2000/svg">
    <defs>
      <linearGradient id="grassTone" x1="0" y1="0" x2="1" y2="1">
        <stop offset="0" stop-color="var(--grass-light)"/>
        <stop offset="0.5" stop-color="var(--grass-dark)"/>
        <stop offset="1" stop-color="var(--grass-light)"/>
      </linearGradient>
    </defs>
    <rect class="lawn-photo" role="img" aria-label="Close-up photo of lush green lawn grass" x="0" y="0" width="584" height="755" fill="url(#grassTone)"/>

    <!-- top wave -->
    <path class="fill-blue" d="M0,0 H584 V100 C540,105 480,125 400,165 C260,230 140,235 0,165 Z"/>
    <path class="fill-green" d="M0,0 H584 V40 C540,45 480,70 400,120 C260,200 140,210 0,130 Z"/>
    <path class="fill-paper" d="M0,0 H584 V30 C540,35 480,60 400,110 C260,190 140,200 0,120 Z"/>

    <!-- bottom wave -->
    <path class="fill-paper" d="M0,610 C120,670 230,670 350,610 C450,565 530,540 584,538 V755 H0 Z"/>
    <path class="fill-green" d="M0,625 C120,695 240,690 360,635 C460,590 530,565 584,560 V755 H0 Z"/>
    <path class="fill-blue" d="M0,650 C120,700 250,700 380,650 C460,625 530,620 584,620 V755 H0 Z"/>

    <!-- brand -->
    <text class="brand-name" x="56" y="95" font-size="42">TurfVent</text>
    <text class="brand-tagline" x="58" y="105" font-size="7">Fresh Air For Stronger Roots.</text>

    <!-- contact -->
    <text class="contact-line" x="558" y="698" text-anchor="end">HELLO@TURFVENT.COM</text>
    <text class="contact-line" x="558" y="728" text-anchor="end">WWW.TURFVENT.COM</text>
    <text class="contact-line" x="33" y="728">+ 202-555-0147</text>
  </svg>
</section>

<!-- Back of the doorknob flyer: field estimate form -->
<section class="flyer-page flyer-back">
  <svg viewBox="0 0 584 755" xmlns="http://www.w3.org/2000/svg">
    <defs>
      <linearGradient id="grassToneBack" x1="0" y1="0" x2="1" y2="0">
        <stop offset="0" stop-color="var(--grass-dark)"/>
        <stop offset="0.5" stop-color="var(--grass-light)"/>
        <stop offset="1" stop-color="var(--grass-dark)"/>
      </linearGradient>
    </defs>

    <!-- top band -->
    <rect class="lawn-photo" role="img" aria-label="Strip of green lawn grass" x="0" y="0" width="584" height="140" fill="url(#grassToneBack)"/>
    <path class="fill-paper" d="M0,75 C150,70 300,110 450,90 C520,80 560,70 584,60 V760 H0 Z"/>
    <path class="fill-green" d="M0,115 C120,95 230,90 330,110 C450,135 530,115 584,105 V760 H0 Z"/>
    <path class="fill-blue" d="M0,123 C120,103 230,98 330,118 C450,143 530,123 584,113 V760 H0 Z"/>
    <path class="fill-paper" d="M0,147 C150,147 250,190 400,185 C500,182 550,175 584,170 V760 H0 Z"/>

    <!-- bottom band -->
    <path class="fill-blue" d="M0,595 C100,590 200,610 300,635 C420,665 500,640 584,630 V755 H0 Z"/>
    <path class="fill-green" d="M0,668 C150,680 300,700 430,690 C500,684 550,668 584,660 V755 H0 Z"/>
    <path class="fill-paper" d="M0,676 C150,688 300,708 430,698 C500,692 550,676 584,668 V755 H0 Z"/>
    <path class="lawn-photo" role="img" aria-label="Strip of green lawn grass" fill="url(#grassToneBack)" d="M0,740 C150,690 300,690 430,700 C500,705 550,695 584,690 V755 H0 Z"/>

    <!-- brand -->
    <text class="brand-name" x="98" y="222" font-size="21">TurfVent</text>
    <text class="brand-tagline" x="99" y="228" font-size="3.6">Fresh Air For Stronger Roots.</text>

    <!-- form fields -->
    <g class="estimate-form">
      <rect class="field-box" x="44" y="273" width="246" height="30" rx="9"/>
      <path class="fill-blue" d="M53,274 H115 V302 H53 A8,8 0 0 1 45,294 V282 A8,8 0 0 1 53,274 Z"/>
      <text class="field-label" x="50" y="292">FIRST NAME</text>

      <rect class="field-box" x="297" y="273" width="243" height="30" rx="9"/>
      <path class="fill-blue" d="M306,274 H368 V302 H306 A8,8 0 0 1 298,294 V282 A8,8 0 0 1 306,274 Z"/>

      <rect class="field-box" x="44" y="318" width="282" height="30" rx="9"/>
      <path class="fill-blue" d="M53,319 H115 V347 H53 A8,8 0 0 1 45,339 V327 A8,8 0 0 1 53,319 Z"/>
      <text class="field-label" x="54" y="337">EMAIL</text>

      <rect class="field-box" x="333" y="318" width="207" height="30" rx="9"/>
      <path class="fill-blue" d="M342,319 H404 V347 H342 A8,8 0 0 1 334,339 V327 A8,8 0 0 1 342,319 Z"/>
      <text class="field-label" x="342" y="337">PHONE</text>

      <rect class="field-box" x="44" y="363" width="496" height="30" rx="9"/>
      <path class="fill-blue" d="M53,364 H115 V392 H53 A8,8 0 0 1 45,384 V372 A8,8 0 0 1 53,364 Z"/>
      <text class="field-label" x="61" y="382">ADRESS</text>

      <rect class="field-box" x="44" y="408" width="496" height="30" rx="9"/>

      <rect class="field-box" x="44" y="453" width="155" height="30" rx="9"/>
      <path class="fill-blue" d="M53,454 H80 V482 H53 A8,8 0 0 1 45,474 V462 A8,8 0 0 1 53,454 Z"/>
      <text class="field-label" x="52" y="472">CITY</text>

      <rect class="field-box" x="206" y="453" width="156" height="30" rx="9"/>
      <path class="fill-blue" d="M215,454 H249 V482 H215 A8,8 0 0 1 207,474 V462 A8,8 0 0 1 215,454 Z"/>
      <text class="field-label" x="212" y="472">STATE</text>

      <rect class="field-box" x="369" y="453" width="171" height="30" rx="9"/>
      <path class="fill-blue" d="M378,454 H428 V482 H378 A8,8 0 0 1 370,474 V462 A8,8 0 0 1 378,454 Z"/>
      <text class="field-label" x="374" y="472">ZIP CODE</text>

      <rect class="field-box" x="44" y="498" width="161" height="30" rx="9"/>
      <path class="fill-blue" d="M53,499 H92 V527 H53 A8,8 0 0 1 45,519 V507 A8,8 0 0 1 53,499 Z"/>
      <text class="field-label" x="52" y="517">SQ FT</text>
    </g>
  </svg>
</section>

</body>
</html>
```